LoreCrate.com how-it-works animated video

We need a video animation and illustrations for the LoreCrate.com home page that show how our knowledge automation framework works.

Please read https://www.lorecrate.com/knowledge-is-stories and see https://www.lorecrate.com/home and for more information.

I strongly advise to follow the 5 minute quick start at https://www.lorecrate.com/quick-start before you start.

Target Market(s)

Professionals. Early adopters.

Industry/Entity Type

Information Technology

Font styles to use
Other font styles liked:
• Roboto

Colors

Designer to choose colors to be used in the design.

Requirements
Must have
• The animation/ilustrations must be easy to understand, match our design style and illustrate the following 6 activities of Experts, Constructs, and Consumers:
• 1) experts automating their knowledge by designing flow charts for free
• 2) flow charts are turned into constructs (robots) for free
• 3) constructs being published to the public stage for free
• 4) consumers starting sessions with constructs for free
• 5) constructs being published to the public stage for a small fee
• 6) consumers starting sessions with constructs for a small free
• 7) low cost organizational membership where constructs can shared within groups
Nice to have
• Flat Design Style
• See attached color scheme #235B7B #86BBD8 #A1E8AF #B5BEC6 #F6AE2D

```html
<!DOCTYPE html>
<html lang="en">
<head>
<meta charset="utf-8">
<title>LoreCrate — How It Works</title>
<link rel="stylesheet" href="https://fonts.googleapis.com/css2?family=Roboto:wght@700;900&display=swap">
<style>
  :root {
    --sky: #3dd4fd;
    --navy: #114a6e;
    --label: #0f4a6e;
    --blue: #0277c0;
    --bright-blue: #1e6ff0;
    --yellow: #f9be3b;
    --green: #4aee96;
    --white: #ffffff;
  }
  * { box-sizing: border-box; margin: 0; padding: 0; }
  html, body {
    width: 1200px; height: 675px; overflow: hidden;
    background: var(--sky);
  }
  .stage {
    position: relative; width: 1200px; height: 675px;
    background: var(--sky);
    font-family: "Roboto", Arial, sans-serif;
  }
  .brand {
    position: absolute; left: 64px; top: 92px;
    display: flex; align-items: center; gap: 12px;
  }
  .brand-mark {
    width: 38px; height: 38px; background: var(--label);
  }
  .brand-name {
    font-size: 30px; font-weight: 900; color: var(--label);
    letter-spacing: -0.5px;
  }
  .figure {
    position: absolute; border-radius: 46px 46px 10px 10px;
  }
  .figure-expert-1 { left: 88px;  top: 262px; width: 116px; height: 318px; background: var(--navy); }
  .figure-expert-2 { left: 407px; top: 262px; width: 118px; height: 318px; background: var(--blue); }
  .figure-construct { left: 697px; top: 267px; width: 98px; height: 311px; background: var(--yellow); }
  .figure-consumer { left: 960px; top: 262px; width: 100px; height: 320px; background: var(--green); }
  .role-label {
    position: absolute; top: 604px; width: 200px; margin-left: -100px;
    text-align: center; font-size: 19px; font-weight: 700;
    color: var(--label); letter-spacing: 0.2px;
  }
  .flow-arrow, .speech {
    position: absolute; width: 105px; height: 58px; overflow: visible;
  }
  .flow-column { left: 559px; }
  .talk-column { left: 825px; }
</style>
</head>
<body>
<main class="stage">
  <div class="brand">
    <span class="brand-mark"></span>
    <span class="brand-name">LoreCrate</span>
  </div>

  <div class="figure figure-expert-1" role="img" aria-label="Illustration of the first expert in a suit"></div>
  <div class="figure figure-expert-2" role="img" aria-label="Illustration of the second expert in a suit"></div>
  <div class="figure figure-construct" role="img" aria-label="Illustration of a construct robot figure"></div>
  <div class="figure figure-consumer" role="img" aria-label="Illustration of a consumer"></div>

  <svg width="0" height="0" style="position:absolute">
    <defs>
      <linearGradient id="grad-navy-blue" x1="0" x2="1">
        <stop offset="0.1" stop-color="#114a6e"/>
        <stop offset="1" stop-color="#1e6ff0"/>
      </linearGradient>
      <linearGradient id="grad-blue-yellow" x1="0" x2="1">
        <stop offset="0" stop-color="#0277c0"/>
        <stop offset="0.65" stop-color="#f9be3b"/>
      </linearGradient>
      <linearGradient id="grad-yellow-green" x1="0" x2="1">
        <stop offset="0.1" stop-color="#f9be3b"/>
        <stop offset="0.8" stop-color="#4aee96"/>
      </linearGradient>
    </defs>
  </svg>

  <!-- Flow arrows: expert to construct -->
  <svg class="flow-arrow flow-column" style="top:63px" viewBox="0 0 112 62">
    <path d="M1,16 H78 V1 L111,31 L78,61 V46 H1 Z" fill="none" stroke="var(--white)" stroke-width="2" stroke-dasharray="2 3"/>
  </svg>
  <svg class="flow-arrow flow-column" style="top:144px" viewBox="0 0 112 62">
    <path d="M1,16 H78 V1 L111,31 L78,61 V46 H1 Z" fill="none" stroke="var(--blue)" stroke-width="2"/>
  </svg>
  <svg class="flow-arrow flow-column" style="top:224px" viewBox="0 0 112 62">
    <path d="M0,16 H78 V0 L112,31 L78,62 V46 H0 Z" fill="var(--blue)"/>
  </svg>
  <svg class="flow-arrow flow-column" style="top:304px" viewBox="0 0 112 62">
    <path d="M0,16 H78 V0 L112,31 L78,62 V46 H0 Z" fill="url(#grad-navy-blue)"/>
  </svg>
  <svg class="flow-arrow flow-column" style="top:388px" viewBox="0 0 112 62">
    <path d="M0,16 H78 V0 L112,31 L78,62 V46 H0 Z" fill="url(#grad-blue-yellow)"/>
  </svg>

  <!-- Speech bubbles: construct to consumer -->
  <svg class="speech talk-column" style="top:62px" viewBox="0 0 110 62">
    <path d="M1,1 H109 V44 H98 L109,62 L70,44 H1 Z" fill="none" stroke="var(--white)" stroke-width="2" stroke-dasharray="2 3"/>
  </svg>
  <svg class="speech talk-column" style="top:142px" viewBox="0 0 110 62">
    <path d="M1,1 H109 V44 H40 L1,62 L12,44 H1 Z" fill="none" stroke="var(--yellow)" stroke-width="2"/>
  </svg>
  <svg class="speech talk-column" style="top:222px" viewBox="0 0 110 62">
    <path d="M0,0 H110 V44 H70 L110,62 L98,44 Z" fill="var(--green)"/>
    <rect x="0" y="0" width="110" height="44" fill="var(--green)"/>
  </svg>
  <svg class="speech talk-column" style="top:302px" viewBox="0 0 110 62">
    <rect x="0" y="0" width="110" height="46" fill="var(--yellow)"/>
    <path d="M10,44 L0,64 L44,44 Z" fill="var(--yellow)"/>
  </svg>
  <svg class="flow-arrow talk-column" style="top:388px" viewBox="0 0 112 62">
    <path d="M0,16 H78 V0 L112,31 L78,62 V46 H0 Z" fill="url(#grad-yellow-green)"/>
  </svg>

  <p class="role-label" style="left:146px">EXPERT 1</p>
  <p class="role-label" style="left:467px">EXPERT 2</p>
  <p class="role-label" style="left:745px">CONSTRUCT</p>
  <p class="role-label" style="left:1009px">CONSUMER</p>
</main>
</body>
</html>
```